Website for Community Storage Startup Company

We're looking for a great design that looks good on mobile devices (as well as the web) - Layout should be responsive and able to scale to many sized devices.

It should provide a good user-experience for people browsing the site with heavy focus on search and search results pages - It should be extremely easy to search, see results and add your own information.

Search parameters should be Location (Text), Dates (Calendar pop up), Price (slider) with optional extra parameters to be displayed (You can just call them Parameter1, Parameter2 etc. for Examples- we'd like to see options of no extra parameters and up to 4 others)

Please include a favicon for the site - we've provided the logo we had designed.

Pages We Must Have:

1) Home Page
2) Search Page (most likely map based)
3) Search Results Page (most likely map based) - we want the search options/results to slide in and out as appropriate - please visualize
Information Page - this is branded and would present information for many possible pages like Terms & Conditions or a FAQ page etc.
4) My Account Page - Should be an inline editable page with Name/Address/Financial information etc. showing
5) Sign-up Page - This could be a slide in element on another page or part of the account page, or separate as you think works best

Ideally this would all work like a single page app with a common theme but we're interested to see your ideas of tying pages together or keeping them separate while fitting our brief.

Examples of things we like;

a) roostly - mobile and web based layouts - we like the map on the side and data input on the other side
b) http://www.zu-o.com/zo/airlines/ - scroll down slightly to the first video - about 0:28 in we like the map on the side and the panel on the side with details you can refine etc. All over we like the site presented through the video

Nice to Have:
- The ability to provide the finished design as sliced CSS, HTML and JS

Reason: Feedback has suggested that the timeline is too tight, we've extended it but are very interested in seeing initial page designs sooner rather than later to provide feedback. Thanks!

Thanks for your contributions so far :)  We've come to realize that in general we're preferring darker color schemes - if you're pulling colors from our logo try to stick to the text colors :)

We like narrow headers and footers and a map based interface. Sliders for information are good and we'd like to see how checkbox elements would play out too.

Examples of how information may pop up from markers would be nice too.

Thanks for everything so far!

Target Market(s)

Young to middle aged adults in the USA

Industry/Entity Type

Airlines

Font styles to use
Sans Serif

Colors

Designer to choose colors to be used in the design.

Requirements
Must have
• 1) Home Page
Nice to have
• The ability to provide the finished design as sliced CSS, HTML and JS

We think a map with markers should figure heavily in search results and searching.

```html
<!DOCTYPE html>
<html lang="en">
<head>
<meta charset="utf-8">
<title>Stowvana — Find Storage Space Near You</title>
<link href="https://fonts.googleapis.com/css2?family=Open+Sans:ital,wght@0,400;0,600;0,700;1,400&family=Nunito+Sans:wght@400;600;700&display=swap" rel="stylesheet">
<style>
:root{
  --teal:#1d8fb8;
  --green:#5aa82a;
  --green-dark:#3f8a19;
  --hero-dark:#0b3f78;
  --hero-light:#1f78b6;
  --ink:#222;
  --grey:#555;
  --grey-light:#8a8a8a;
  --sky:#aecbd6;
  --link:#2a7fb0;
  --footer:#4a4a4a;
  --footer-text:#cfcfcf;
  --white:#fff;
}
*{box-sizing:border-box;margin:0;padding:0}
html,body{width:874px;height:1200px;overflow:hidden;background:var(--white)}
body{font-family:"Open Sans",Arial,sans-serif;color:var(--ink);position:relative}
.abs{position:absolute}
a{color:inherit;text-decoration:none}

/* header */
.topline{left:0;top:0;width:874px;height:3px;background:var(--teal)}
.site-header{left:0;top:3px;width:874px;height:98px;background:var(--white);border-bottom:2px solid #dcdcdc}
.brand{left:94px;top:46px;display:flex;align-items:center;gap:8px;font-family:"Nunito Sans",sans-serif;font-size:28px;font-weight:400;color:#3a3a3a}
.brand-mark{width:22px;height:22px;background:var(--teal)}
.account-link{left:605px;top:24px;font-size:10.5px;color:#333}
.signup-btn{left:675px;top:15px;width:110px;height:28px;background:linear-gradient(#66b832,var(--green-dark));border-radius:3px;color:var(--white);font-size:10.5px;font-weight:700;display:flex;align-items:center;justify-content:center;gap:8px}
.signup-btn svg{width:12px;height:14px}
.main-nav{left:370px;top:64px;display:flex;font-size:9.5px;color:#555;letter-spacing:.3px}
.main-nav a{padding:0 19px;border-left:1px solid #bbb;line-height:13px}
.main-nav a:first-child{border-left:none}

/* hero */
.hero{left:0;top:102px;width:874px;height:328px;background:radial-gradient(ellipse at 30% 30%,var(--hero-light),var(--hero-dark) 85%)}
.hero-photo{left:432px;top:102px;width:442px;height:328px;background:linear-gradient(110deg,#c9a57e 0%,#e7d3b8 35%,#9bb7d6 70%,#cfb08a 100%)}
.hero-title{left:94px;top:184px;font-family:"Nunito Sans",sans-serif;font-size:22px;font-weight:600;color:var(--white)}
.search-box{left:93px;top:220px;width:325px;height:38px;background:var(--white);border-radius:3px}
.search-fields{left:101px;top:227px;width:247px;height:24px;border:1px solid #ddd;display:flex;font-size:9px;color:#666}
.search-fields span{display:flex;align-items:center;gap:5px;padding-left:7px;border-right:1px dotted #bbb}
.search-fields span:last-child{border-right:none}
.search-fields svg{width:9px;height:10px}
.find-btn{left:358px;top:227px;width:52px;height:24px;background:linear-gradient(#66b832,var(--green-dark));color:var(--white);font-size:10px;font-weight:700;display:flex;align-items:center;justify-content:center;border-radius:2px}
.size-help{left:94px;top:266px;font-size:11px;font-style:italic;color:#7cc6ee}
.list-facility{left:94px;top:298px;font-size:10px;font-weight:600;color:var(--white)}

/* stats */
.stats{left:0;top:430px;width:874px;height:81px;background:var(--white);display:flex;padding-left:94px}
.stat{height:81px;display:flex;align-items:center;gap:12px;border-right:1px solid #ddd}
.stat:last-child{border-right:none}
.stat svg{width:32px;height:40px}
.stat-text{text-align:center;font-family:"Nunito Sans",sans-serif;color:#6a6a6a;line-height:1.1}
.stat-text b{display:block;font-size:20px;font-weight:700;color:#5a5a5a}
.stat-text span{font-size:16px}

/* testimonials */
.reviews{left:0;top:511px;width:874px;height:297px;background:var(--sky)}
.reviews h2{left:94px;top:534px;font-family:"Nunito Sans",sans-serif;font-size:19px;font-weight:600;color:#1e1e1e}
.quote{top:584px;width:225px;height:116px;background:var(--white);padding:13px 16px;font-size:9.2px;font-style:italic;line-height:14.5px;color:#333}
.quote::after{content:"";position:absolute;bottom:-7px;right:40px;border:7px solid transparent;border-bottom:0;border-top-color:var(--white)}
.quote-name{top:716px;font-size:9px;color:#333}
.rating{left:0;top:758px;width:874px;text-align:center;font-size:12.5px;color:#222}
.rating a{color:var(--link)}

/* features */
.feature{top:843px;width:207px}
.feature-img{width:207px;height:98px;border:1px solid #ddd;padding:4px;background:var(--white)}
.feature-img div{width:100%;height:100%}
.feature p{text-align:center;margin-top:13px;font-family:"Nunito Sans",sans-serif;font-size:14px;font-weight:600;color:#333}

/* footer */
.site-footer{left:0;top:992px;width:874px;height:173px;background:var(--footer)}
.f-col{top:1019px}
.f-col h3{font-family:"Nunito Sans",sans-serif;font-size:12px;font-weight:700;color:var(--white);padding-bottom:5px;border-bottom:1px solid #777;margin-bottom:10px;display:inline-block;padding-right:22px}
.f-col li{list-style:none;font-size:9.5px;color:var(--footer-text);line-height:19px}
.social li{display:flex;align-items:center;gap:7px;line-height:27px}
.social i{width:19px;height:19px;border-radius:50%;background:#666;display:inline-block}
.contact{border-left:1px solid #5c5c5c;padding-left:17px}
.contact p{font-size:9.5px;color:var(--footer-text);line-height:17px;width:190px}
.bottom-bar{left:94px;top:1175px;width:690px;display:flex;justify-content:space-between;font-size:9px;color:#333}
</style>
</head>
<body>
<div class="abs topline"></div>
<header class="abs site-header"></header>
<div class="abs brand"><span class="brand-mark"></span>Stowvana</div>
<a class="abs account-link" href="#">My Account</a>
<a class="abs signup-btn" href="#"><svg viewBox="0 0 12 14"><rect x="1" y="1" width="10" height="12" fill="none" stroke="#fff" stroke-width="1.5"/><path d="M3 5h6M3 8h6M3 11h4" stroke="#fff"/></svg>SIGN UP NOW</a>
<nav class="abs main-nav"><a href="#">HOME</a><a href="#">SEARCH</a><a href="#">INFORMATION</a><a href="#">ABOUT US</a><a href="#">CONTACT US</a></nav>

<section class="abs hero"></section>
<div class="abs hero-photo" role="img" aria-label="Smiling couple stacking cardboard moving boxes"></div>
<h1 class="abs hero-title">Find Storage Space Near You</h1>
<div class="abs search-box"></div>
<div class="abs search-fields">
  <span style="width:108px"><svg viewBox="0 0 9 10"><path d="M4.5 0a3.5 3.5 0 0 1 3.5 3.5C8 6 4.5 10 4.5 10S1 6 1 3.5A3.5 3.5 0 0 1 4.5 0z" fill="#8a8fb8"/></svg>location</span>
  <span style="width:72px"><svg viewBox="0 0 9 10"><rect x="0.5" y="1.5" width="8" height="8" fill="none" stroke="#999"/><path d="M0.5 4h8" stroke="#999"/></svg>Date</span>
  <span style="width:67px"><b style="color:#6b78b0">$</b>Price ▴▾</span>
</div>
<a class="abs find-btn" href="#">FIND</a>
<a class="abs size-help" href="#">What size of storage do i need?</a>
<a class="abs list-facility" href="#">▸&nbsp; List your Storage Facitlity on Stowvana</a>

<section class="abs stats">
  <div class="stat" style="width:152px"><svg viewBox="0 0 32 40"><path d="M16 2a12 12 0 0 1 12 12c0 9-12 24-12 24S4 23 4 14A12 12 0 0 1 16 2z" fill="#9a9a9a"/><circle cx="16" cy="14" r="5" fill="#fff"/></svg><div class="stat-text"><b>2,000+</b><span>locations</span></div></div>
  <div class="stat" style="width:190px;padding-left:30px"><svg viewBox="0 0 32 40"><path d="M10 14L16 6l6 8" fill="none" stroke="#9a9a9a" stroke-width="2"/><circle cx="16" cy="5" r="2.5" fill="#9a9a9a"/><rect x="2" y="14" width="28" height="20" rx="3" fill="#9a9a9a"/><text x="16" y="28" font-size="9" font-weight="700" fill="#fff" text-anchor="middle" font-family="Open Sans,sans-serif">OPEN</text></svg><div class="stat-text"><b>6 Days</b><span>a week</span></div></div>
  <div class="stat" style="width:190px;padding-left:22px"><svg viewBox="0 0 40 40" style="width:40px"><circle cx="17" cy="18" r="14" fill="none" stroke="#9a9a9a" stroke-width="3"/><path d="M17 9v9h7" fill="none" stroke="#9a9a9a" stroke-width="3"/><rect x="20" y="24" width="12" height="9" fill="#9a9a9a"/><path d="M32 27h5l2 3v3h-7z" fill="#9a9a9a"/><circle cx="24" cy="35" r="2.5" fill="#9a9a9a"/><circle cx="35" cy="35" r="2.5" fill="#9a9a9a"/></svg><div class="stat-text"><b>24 Hours</b><span>Delivery</span></div></div>
  <div class="stat" style="width:170px;padding-left:30px"><svg viewBox="0 0 32 40"><path d="M8 18v-6a8 8 0 0 1 16 0v6" fill="none" stroke="#9a9a9a" stroke-width="4"/><rect x="4" y="18" width="24" height="20" rx="2" fill="#9a9a9a"/><rect x="14" y="24" width="4" height="8" fill="#fff"/></svg><div class="stat-text"><b>Secure</b><span>Service</span></div></div>
</section>

<section class="abs reviews"></section>
<h2 class="abs" style="left:94px;top:534px;font-family:'Nunito Sans',sans-serif;font-size:19px;font-weight:600;color:#1e1e1e">What Our Customers Say</h2>
<blockquote class="abs quote" style="left:93px">Integer vehicula velit quis ante ornare iaculis. Sed sed neque metus. Nullam mauris metus,Integer vehicula velit quis ante ornare iaculis. Sed sed neque metus. Nullam mauris metus,Integetr vehicula velit quis ante ornare</blockquote>
<blockquote class="abs quote" style="left:326px">Integer vehicula velit quis ante ornare iaculis. Sed sed neque metus. Nullam mauris metus,Integer vehicula velit quis ante ornare iaculis. Sed sed neque metus. Nullam mauris metus,Integetr vehicula velit quis ante ornare</blockquote>
<blockquote class="abs quote" style="left:558px">Integer vehicula velit quis ante ornare iaculis. Sed sed neque metus. Nullam mauris metus,Integer vehicula velit quis ante ornare iaculis. Sed sed neque metus. Nullam mauris metus,Integetr vehicula velit quis ante ornare</blockquote>
<p class="abs quote-name" style="left:245px">Mara Quill</p>
<p class="abs quote-name" style="left:472px">Jenna Holt</p>
<p class="abs quote-name" style="left:702px">Rosa Keller</p>
<p class="abs rating"><b>Stowvana</b> has been rated 9.4 out of 10 based on 2,524 reviews. <a href="#">See the reviews</a></p>

<div class="abs feature" style="left:94px"><div class="feature-img"><div role="img" aria-label="Corridor of blue roll-up storage unit doors" style="background:linear-gradient(90deg,#1f4f9a,#cfd8e4 50%,#1f4f9a)"></div></div><p>Large Space Online</p></div>
<div class="abs feature" style="left:335px"><div class="feature-img"><div role="img" aria-label="Open storage unit with blue doors" style="background:linear-gradient(90deg,#2d5c86,#b9cfe0 55%,#1e4a7a)"></div></div><p>Find the Best Deals</p></div>
<div class="abs feature" style="left:576px"><div class="feature-img"><div role="img" aria-label="Tidy garage with a car and a motorcycle" style="background:linear-gradient(180deg,#efe9e2,#c9c3bc)"></div></div><p>Storage Made Easy</p></div>

<footer class="abs site-footer"></footer>
<div class="abs f-col" style="left:103px"><h3>RESOURCES</h3><ul><li>Resources</li><li>Competition</li><li>Data Storage</li><li>Location</li></ul></div>
<div class="abs f-col" style="left:220px"><h3>ABOUT US</h3><ul><li>Affiliate Program</li><li>FAQ</li><li>About Us</li><li>Contact Us</li></ul></div>
<div class="abs f-col" style="left:342px"><h3>COMMUNITY</h3><ul><li>Returns/Exchanges</li><li>Privacy</li><li>Warranty Information</li><li>Become A Distributor</li></ul></div>
<div class="abs f-col" style="left:471px"><h3>FOLLOW US</h3><ul class="social"><li><i></i>Blog</li><li><i></i>Chirpline</li><li><i></i>Workweb</li></ul></div>
<div class="abs f-col" style="left:600px"><h3>CONTACT US</h3></div>
<div class="abs contact" style="left:583px;top:1052px"><p>US Phone Numbers 5,550,142 / 5,550,1 Information Sources: Lorem Report justice, Ipsum of Justice Statistics and U.S. Bureau of Records.</p></div>
<div class="abs bottom-bar"><span>Copyrights © 2014 stowvana.com - All Rights Reserved</span><span>Privacy Policy &nbsp; | &nbsp; Terms &amp; Condition</span></div>
</body>
</html>
```